October Billboard TX

Billboard - creative design using company colors. Previous billboard graphic is included for reference along with a rough example of the requested "less busy" design. Required graphics for the simple billboard design are also included in the upload. Billboard dimensions are attached. Need this design ASAP!

```html
<!DOCTYPE html>
<html lang="en">
<head>
<meta charset="utf-8">
<title>October Billboard TX</title>
<link rel="stylesheet" href="https://fonts.googleapis.com/css2?family=Poppins:wght@600;700;800&family=Titan+One&display=swap">
<style>
  :root {
    --stage: #8f8f8f;
    --sky-light: #ffffff;
    --sky: #cdeff8;
    --brand-blue: #0b74b9;
    --logo-blue: #1b7fc9;
    --ink: #1c1c1c;
    --red: #d70f14;
    --red-deep: #9c0c10;
    --yellow: #f7ec3b;
    --white: #ffffff;
  }
  * { margin: 0; padding: 0; box-sizing: border-box; }
  html, body { width: 1200px; height: 707px; overflow: hidden; background: var(--stage); }
  .billboard {
    position: absolute; left: 59px; top: 96px; width: 1082px; height: 541px;
    background: radial-gradient(ellipse at 62% 30%, var(--sky-light) 0%, var(--sky) 75%);
    overflow: hidden;
    font-family: "Poppins", sans-serif;
    box-shadow: 0 6px 18px rgba(0,0,0,.35);
  }
  .brand { position: absolute; left: 62px; top: 50px; display: flex; align-items: center; gap: 10px; z-index: 2; }
  .brand-dot { width: 34px; height: 34px; border-radius: 50%; background: var(--logo-blue); }
  .brand-name { color: var(--logo-blue); font-weight: 700; font-size: 28px; line-height: 1.05; }
  .tagline { position: absolute; left: 61px; top: 158px; color: var(--ink); font-weight: 700; font-size: 19px; line-height: 23px; white-space: nowrap; z-index: 2; }
  .headline { position: absolute; left: 60px; top: 206px; color: var(--red); font-family: "Titan One", sans-serif; font-size: 60px; line-height: 60px; white-space: nowrap; z-index: 2; }
  .headline span { display: block; transform-origin: left center; }
  .headline .line-two { transform: scaleX(0.88); }
  .attribution-rule { position: absolute; left: 61px; top: 336px; width: 226px; height: 1px; background: #9a9a9a; }
  .attribution { position: absolute; left: 293px; top: 322px; color: var(--ink); font-weight: 700; font-size: 18px; z-index: 2; }
  .photo { position: absolute; left: 450px; top: 41px; width: 375px; height: 335px; border-radius: 180px 180px 0 0; z-index: 1;
    background: linear-gradient(160deg, #5a3a2e 0%, #e9b89b 45%, #f3e05a 85%); }
  .audience { position: absolute; left: 840px; top: 64px; list-style: none; }
  .audience li { display: flex; align-items: flex-start; gap: 10px; color: var(--ink); font-weight: 700; font-size: 24px; line-height: 27px; margin-bottom: 27px; }
  .audience li:nth-child(2) { margin-bottom: 26px; }
  .audience svg { flex: none; margin-top: -2px; }
  .band { position: absolute; left: 0; top: 355px; z-index: 2; }
  .cta-label { position: absolute; left: 65px; top: 402px; color: var(--yellow); font-weight: 700; font-size: 27.5px; white-space: nowrap; z-index: 3; }
  .phone-pill { position: absolute; left: 91px; top: 441px; width: 324px; height: 53px; border-radius: 0 10px 10px 0; background: var(--red);
    color: var(--white); font-weight: 700; font-size: 33px; line-height: 53px; padding-left: 38px; white-space: nowrap; z-index: 3; }
  .phone-icon { position: absolute; left: 63px; top: 442px; z-index: 4; }
  .spanish { position: absolute; left: 485px; top: 398px; color: var(--white); font-weight: 600; font-size: 43px; line-height: 47px; white-space: nowrap; z-index: 3; }
  .kids-badge { position: absolute; left: 830px; top: 312px; width: 180px; height: 180px; z-index: 3; }
  .kids-text { position: absolute; left: 830px; top: 362px; width: 180px; text-align: center; font-family: "Titan One", sans-serif; font-size: 37px; line-height: 34px; z-index: 4; }
  .kids-text .kids { color: var(--yellow); display: block; }
  .kids-text .only { color: var(--white); display: block; }
</style>
</head>
<body>
<main class="billboard">
  <div class="brand"><span class="brand-dot"></span><span class="brand-name">Bright Sprouts<br>Eye Clinic</span></div>

  <p class="tagline">I TAKE MY CHILD TO EL PASO'S MOST<br>QUALIFIED AND EXPERIENCED</p>
  <h1 class="headline"><span class="line-one">PEDIATRIC</span><span class="line-two">EYE DOCTOR</span></h1>
  <div class="attribution-rule"></div>
  <p class="attribution">- M. Reyes</p>

  <div class="photo" role="img" aria-label="Photo of a smiling mother hugging her young daughter who wears red glasses and a yellow top"></div>

  <ul class="audience">
    <li><svg width="32" height="32" viewBox="0 0 32 32"><circle cx="16" cy="16" r="16" fill="var(--red)"/><circle cx="16" cy="16" r="9" fill="var(--yellow)"/><path d="M12 16l3 3 5-6" stroke="var(--red)" stroke-width="2" fill="none"/></svg>Newborns</li>
    <li><svg width="32" height="32" viewBox="0 0 32 32"><circle cx="16" cy="16" r="16" fill="var(--red)"/><circle cx="16" cy="16" r="9" fill="var(--yellow)"/><path d="M12 16l3 3 5-6" stroke="var(--red)" stroke-width="2" fill="none"/></svg>Infants</li>
    <li><svg width="32" height="32" viewBox="0 0 32 32"><circle cx="16" cy="16" r="16" fill="var(--red)"/><circle cx="16" cy="16" r="9" fill="var(--yellow)"/><path d="M12 16l3 3 5-6" stroke="var(--red)" stroke-width="2" fill="none"/></svg>Toddlers</li>
    <li><svg width="32" height="32" viewBox="0 0 32 32" style="margin-top:4px"><circle cx="16" cy="16" r="16" fill="var(--red)"/><circle cx="16" cy="16" r="9" fill="var(--yellow)"/><path d="M12 16l3 3 5-6" stroke="var(--red)" stroke-width="2" fill="none"/></svg>Tweens &amp;<br>Teens</li>
  </ul>

  <svg class="band" width="1082" height="186" viewBox="0 0 1082 186">
    <path fill="var(--white)" d="M0 14 L40 6 L80 12 L120 4 L170 14 L220 8 L270 22 L330 10 L380 18 L430 6 L480 14 L540 8 L600 16 L650 6 L700 12 L760 4 L820 14 L880 8 L940 16 L1000 10 L1050 14 L1082 10 L1082 186 L0 186 Z"/>
    <path fill="var(--brand-blue)" d="M0 22 L40 14 L80 20 L120 12 L170 22 L220 16 L270 30 L330 18 L380 26 L430 14 L480 22 L540 16 L600 24 L650 14 L700 20 L760 12 L820 22 L880 16 L940 24 L1000 18 L1050 22 L1082 18 L1082 186 L0 186 Z"/>
  </svg>

  <p class="cta-label">FOR APPOINTMENTS CALL</p>
  <div class="phone-pill">(915) 555-0142</div>
  <svg class="phone-icon" width="52" height="52" viewBox="0 0 52 52">
    <circle cx="26" cy="26" r="25" fill="#1a1a1a" stroke="var(--brand-blue)" stroke-width="2"/>
    <path d="M18 16c2-1 3 0 4 3l1 3c0 1-1 2-2 3 1 3 3 5 6 6 1-1 2-2 3-2l3 1c3 1 4 2 3 4-1 3-4 4-7 3-6-2-11-7-13-13-1-3 0-6 2-8z" fill="var(--white)"/>
  </svg>

  <p class="spanish">La Doctora<br>Habla Español</p>

  <svg class="kids-badge" width="180" height="180" viewBox="0 0 180 180">
    <circle cx="90" cy="90" r="88" fill="var(--red)"/>
    <circle cx="90" cy="90" r="72" fill="var(--red-deep)"/>
  </svg>
  <p class="kids-text"><span class="kids">KIDS</span><span class="only">ONLY</span></p>
</main>
</body>
</html>
```